SloPitch Ad

Looking for a creative eye-catching ad to go on the front page of my website to promote a softball league. Ad dimensions needs to be 1194 by 624, or in that ratio so that it can also be used on facebook.
I have attached some graphics that I have seen on other sites that I like for general ideas. Will need the colors to match with my website (www.pkvathletics.com) but logo is not necessary

```html
<!DOCTYPE html>
<html lang="en">
<head>
<meta charset="utf-8">
<title>Softball Leagues Now Open – PKV Athletics</title>
<link rel="stylesheet" href="https://fonts.googleapis.com/css2?family=Montserrat:wght@600;700&family=Roboto:wght@400;700&display=swap">
<style>
  :root {
    --night: #0d0f0c;
    --night-soft: #23261c;
    --turf: #4e5a2a;
    --turf-dark: #2a3218;
    --infield: #9a6a3c;
    --band-green: #6fb043;
    --band-green-dark: #5e9a36;
    --band-white: #eeeeee;
    --ink: #2b2b2b;
    --white: #ffffff;
    --gold: #f2d35a;
    --brand: #ece8a8;
    --button-top: #6cc224;
    --button-bottom: #3f8f0c;
  }
  * { margin: 0; padding: 0; box-sizing: border-box; }
  html, body { width: 1200px; height: 627px; overflow: hidden; background: var(--night); }
  .ad {
    position: relative;
    width: 1200px;
    height: 627px;
    overflow: hidden;
    font-family: "Montserrat", sans-serif;
  }
  .stadium-photo {
    position: absolute;
    inset: 0;
    background:
      radial-gradient(ellipse 330px 120px at 820px 290px, var(--infield) 0%, rgba(154,106,60,0.55) 60%, rgba(154,106,60,0) 100%),
      linear-gradient(180deg, var(--night) 0%, var(--night-soft) 28%, var(--turf-dark) 40%, var(--turf) 60%, var(--turf-dark) 80%, var(--night) 100%);
  }
  .stadium-photo::after {
    content: "";
    position: absolute;
    inset: 0;
    background: linear-gradient(90deg, rgba(0,0,0,0.45) 0%, rgba(0,0,0,0.1) 55%, rgba(0,0,0,0.25) 100%);
  }
  .bands { position: absolute; inset: 0; }
  .headline {
    position: absolute;
    left: 84px;
    top: 104px;
    color: var(--white);
    font-weight: 600;
    text-transform: uppercase;
    line-height: 1;
  }
  .headline-top { display: block; font-size: 43px; letter-spacing: 0.5px; word-spacing: 10px; }
  .headline-main { display: block; font-size: 80px; margin-top: 14px; letter-spacing: 0.5px; }
  .register-button {
    position: absolute;
    left: 87px;
    top: 260px;
    width: 315px;
    height: 43px;
    display: flex;
    align-items: center;
    justify-content: center;
    background: linear-gradient(180deg, var(--button-top), var(--button-bottom));
    color: var(--white);
    font-family: "Roboto", sans-serif;
    font-size: 21px;
    text-decoration: none;
  }
  .brand-name {
    position: absolute;
    right: 44px;
    top: 30px;
    color: var(--brand);
    font-family: "Montserrat", sans-serif;
    font-weight: 700;
    font-size: 36px;
  }
  .band-text {
    position: absolute;
    left: 0;
    width: 1200px;
    text-align: center;
    transform: rotate(-2.4deg);
    font-family: "Roboto", sans-serif;
    font-weight: 700;
  }
  .tagline { top: 396px; font-size: 26px; color: var(--ink); }
  .league-title { top: 462px; font-size: 50px; color: var(--ink); }
  .band-brand { top: 539px; font-size: 30px; color: var(--white); }
</style>
</head>
<body>
  <main class="ad">
    <div class="stadium-photo" role="img" aria-label="Night-time floodlit softball stadium with players on the field"></div>

    <svg class="bands" width="1200" height="627" viewBox="0 0 1200 627" aria-hidden="true">
      <polygon points="0,420 1200,370 1200,425 0,475" fill="var(--band-green)"/>
      <polygon points="0,475 1200,425 1200,505 0,555" fill="var(--band-white)"/>
      <polygon points="0,555 1200,505 1200,627 0,627" fill="var(--night)" opacity="0.55"/>
      <polygon points="0,583 470,564 470,567 0,587" fill="var(--gold)"/>
      <polygon points="0,592 480,572 480,574 0,595" fill="var(--white)"/>
      <polygon points="0,600 470,580 470,583 0,604" fill="var(--gold)"/>
      <polygon points="720,552 1200,532 1200,536 720,555" fill="var(--gold)"/>
      <polygon points="710,560 1200,540 1200,542 710,562" fill="var(--white)"/>
      <polygon points="720,568 1200,548 1200,552 720,571" fill="var(--gold)"/>
    </svg>

    <div class="brand-name">PKV Athletics</div>

    <h1 class="headline">
      <span class="headline-top">Softball Leagues</span>
      <span class="headline-main">Now Open</span>
    </h1>

    <a class="register-button" href="#">Register now</a>

    <p class="band-text tagline">Lets Play</p>
    <p class="band-text league-title">Softball league</p>
    <p class="band-text band-brand">PKV Athletics</p>
  </main>
</body>
</html>
```